Verdant Row

Currently www.verdantrow-example.com. This site was designed with a generic templet. However it is functional. I'm looking for a fun, fresh, and professional design. I also need help getting the XML for Searchly and Findo. I'm not a web designer and need help. I do not like my current sites narrow width.
Updates

All and all I'm liking the designs. The earlier ones seem better. Some seem that they are just taking my images and inputing them into a templet. I could have done that. The pictures are nice. Please keep in mind, functionality and updates. Please help us show our customers our how we are different. Safe Reliable Responsible are the key fundamentals, inside of these fundamentals show that were are customer service specialized. We are, Licensed, Insured, Drug Screened, Criminally Screened. Seems that people are putting up nice pictures but not capturing our values. Please help us market us on our website. Show our prospective customers why we are better, how we differentiate ourself from the competitors. Why choose us? Our flyers and cards are designed to drive our prospective customers to the website. If it looks identical with no pazaz like the card, then the marketing chain failed. I included our cards to help guide the thought process of our company. The link below is a feature I would love to have. This may be another project itself. I'm not sure if PH is the place to accomplish it. Below is a link for people to estimate there lawns with globe viewer. I would like to give a range of estimates using this technology. I have no clue how to accomplish it. If anyone knows how to who could do this, Please let me know. https://www.yardquote-example.com/showOrder/MOWLAWN/propertyDetails

Target Market(s)

We target residential customers 30-80 yr old. We also are expanding and placing a special emphasis on Business accounts. The main service is a mowing and landscape maintenance. Should be the main focus of the site.

Industry/Entity Type

Searchly

Coding

Coded - Design and coding required

Font styles to use
Sans Serif

Requirements
Must have
• I want this site to be fun and colorful. It still needs to be professional looking as not to deter business accounts. If you use photos, they must reflect Florida lawn. Note the architecture the homes, grass type, types of plants.
Should not have
• My current site is ok. I use it just as a

```html
<!DOCTYPE html>
<html lang="en">
<head>
<meta charset="utf-8">
<title>Verdant Row — Lawn Care</title>
<link href="https://fonts.googleapis.com/css2?family=Archivo+Black&family=Arimo:wght@400;700&family=Roboto+Condensed:wght@400;700&display=swap" rel="stylesheet">
<style>
:root{
  --green:#5fa92b;
  --green-dark:#3f8a1c;
  --green-light:#9ccb62;
  --red:#e8402a;
  --ink:#333;
  --muted:#666;
  --header:#141414;
  --sky:#e6f3f8;
  --soil:#7b5a3e;
}
*{box-sizing:border-box;margin:0;padding:0}
html,body{width:960px;height:1200px;overflow:hidden}
body{position:relative;font-family:"Arimo",sans-serif;color:var(--ink);background:linear-gradient(180deg,#fff 460px,var(--sky) 640px,#f4fafc 1000px)}
.abs{position:absolute;white-space:nowrap}

/* header */
.site-header{left:0;top:0;width:960px;height:94px;background:linear-gradient(180deg,rgba(10,10,10,.95),rgba(25,25,25,.85));z-index:2}
.brand{left:118px;top:26px;color:#fff;font-weight:700;font-size:21px;display:flex;align-items:center;gap:6px}
.brand .dot{width:12px;height:12px;border-radius:50%;background:var(--red)}
.brand-sub{left:118px;top:55px;color:#fff;font-size:10px;font-weight:700;line-height:12px}
.call{right:174px;top:14px;color:#fff;font-size:14px}
.call b{font-weight:700}
.call small{font-size:11px;margin:0 4px;font-weight:700}
.social{top:14px;display:flex;gap:5px;right:112px}
.social i{width:18px;height:18px;border-radius:50%;background:#fff;display:block}
.nav{right:0;width:960px;top:59px;display:flex;justify-content:flex-end;padding-right:122px;gap:6px;font-family:"Roboto Condensed",sans-serif;font-weight:700;font-size:13.5px}
.nav a{color:#ccc;text-decoration:none;padding:5px 12px;border-radius:2px}
.nav a.active{background:var(--green);color:#fff}

/* hero */
.hero{left:0;top:0;width:960px;height:460px;background:radial-gradient(ellipse at 50% 40%,#f0d6b8 0,#c9a27e 22%,#7fae4a 55%,#4e8a22 100%)}
.hero-title{left:120px;top:376px;font-family:"Archivo Black",sans-serif;font-size:20.5px;color:#1c1c1c;letter-spacing:.2px}
.hero-sub{left:120px;top:404px;font-size:11.5px;color:#3a3a3a}
.quote-btn{left:118px;top:422px;width:165px;height:28px;background:var(--red);color:#fff;font-family:"Archivo Black",sans-serif;font-size:18px;padding:2px 0 0 8px}
.dots{left:464px;top:443px;display:flex;gap:5px}
.dots i{width:8px;height:8px;border-radius:50%;background:var(--green-dark);display:block}
.dots i:first-child{background:var(--red)}

/* services */
.service{top:496px;width:166px;text-align:center}
.service .thumb{height:86px}
.service h3{margin-top:6px;font-weight:400;font-size:14px;color:var(--green);line-height:16px}
.service h3 b{display:block;font-family:"Archivo Black",sans-serif;font-weight:400;font-size:13px;letter-spacing:.3px}

/* columns */
.col-head{top:678px;width:260px;text-align:center}
.col-head h2{font-weight:400;font-size:17px;color:var(--green)}
.col-head h2 b{font-family:"Archivo Black",sans-serif;font-weight:400}
.col-head p{font-size:10.5px;color:var(--muted);margin-top:6px}
.map{left:123px;top:734px;width:197px;height:222px;background:linear-gradient(135deg,#dedede,#c8d2d6)}
.link{font-size:11.5px;color:var(--red);text-decoration:underline}
.quote-form{left:381px;top:735px;width:195px}
.field{height:19px;border:1px solid #c9c9c9;background:#fff;margin-bottom:2.7px;font-size:10px;color:#555;padding:3px 6px}
.field.area{height:48px}
.submit{left:511px;top:961px;width:65px;height:22px;background:var(--red);color:#fff;font-size:12px;text-align:center;line-height:22px}
.testimonial{left:631px;top:731px;width:214px;font-size:11.4px;line-height:16.8px;text-align:justify;white-space:normal}
.author{left:634px;top:868px;font-size:9px;color:#555;line-height:15px}
.rule{left:626px;top:906px;width:224px;height:1px;background:#bbb}

/* bottom */
.ground{left:0;top:1040px;width:960px;height:160px}
.banner{left:146px;top:1024px;width:654px;height:54px;background:linear-gradient(90deg,#6c4c33,var(--soil) 60%,#8e6a4a);color:#f3ece4;font-size:12.5px;padding:19px 0 0 15px}
.banner b{font-family:"Archivo Black",sans-serif;font-weight:400}
.turf{left:740px;top:1014px;width:80px;height:70px;border-radius:8px 30px 8px 8px;background:linear-gradient(160deg,#7bbd3a,#4f7c2a 60%,#7a5a3c)}
.foot-links{left:123px;top:1150px;font-family:"Roboto Condensed",sans-serif;font-size:11px;color:#fff;line-height:14px}
.foot-brand{left:582px;width:150px;text-align:center;top:1120px;color:var(--red);font-weight:700;font-size:20px}
.foot-brand-sub{left:572px;top:1150px;color:#fff;font-size:9.5px;font-weight:700;text-align:center;width:170px;line-height:12px}
.address{left:750px;top:1109px;color:#fff;font-size:10px;line-height:12.5px}
.foot-social{left:750px;top:1152px;display:flex;gap:4px}
.foot-social i{width:13px;height:13px;border-radius:50%;background:#fff;display:block}
</style>
</head>
<body>

<div class="hero abs" role="img" aria-label="Photo of a smiling family lying together on a green lawn"></div>

<header class="site-header abs">
  <div class="brand abs"><span class="dot"></span>Verdant Row</div>
  <div class="brand-sub abs">WWW.VERDANTROW-EXAMPLE.COM<br>555-014-7720</div>
  <div class="call abs">Call Us Today! &nbsp;<b>555-014-7720</b><small>or</small><b>555-014-YARD</b></div>
  <div class="social abs"><i></i><i></i></div>
  <nav class="nav abs">
    <a class="active" href="#">HOME</a><a href="#">ABOUT US</a><a href="#">SERVICES</a><a href="#">ESTIMATES</a><a href="#">CONTACT US</a>
  </nav>
</header>

<h1 class="hero-title abs">WE PUT OUR PERSONAL TOUCH ON LAWN CARE</h1>
<p class="hero-sub abs">FOR A REFRESHING LAWN CARE EXPERIENCE CALL 555-014-YARD TODAY.</p>
<div class="quote-btn abs">FREE QUOTE &nbsp;›</div>
<div class="dots abs"><i></i><i></i><i></i></div>

<div class="service abs" style="left:110px"><div class="thumb" role="img" aria-label="Red lawn mower on grass" style="background:linear-gradient(120deg,#d8383a 0,#b73b33 35%,#6a9a3c 55%,#4d7c2c)"></div><h3>PROFESSIONAL<b>LAWN MOWING</b></h3></div>
<div class="service abs" style="left:300px"><div class="thumb" role="img" aria-label="Landscaped garden with flower beds" style="background:linear-gradient(180deg,#2f5a2a,#d4543a 50%,#5e9a36)"></div><h3>LANDSCAPING<b>SERVICES</b></h3></div>
<div class="service abs" style="left:491px"><div class="thumb" role="img" aria-label="Wooden deck being power washed" style="background:linear-gradient(110deg,#5a2f18,#a8693a 45%,#c9b39b 55%,#7a4220)"></div><h3>POWER<b>WASHING</b></h3></div>
<div class="service abs" style="left:682px"><div class="thumb" role="img" aria-label="Park with trimmed trees and lawn" style="background:linear-gradient(180deg,#4b6a2a,#6f9a3a 60%,#8fc050)"></div><h3>TREE TRIMMING<b>AND REMOVAL</b></h3></div>

<div class="col-head abs" style="left:92px"><h2>NOW <b>SERVING</b></h2><p>Click on the map to know about the places</p></div>
<div class="col-head abs" style="left:348px"><h2>GET A <b>FREE QUOTE</b></h2><p>Fill the form to tell us about your project</p></div>
<div class="col-head abs" style="left:608px"><h2>CLIENT <b>TESTIMONIALS</b></h2><p>Let's check what people say about us</p></div>

<div class="map abs" role="img" aria-label="Street map of the service area with marked locations"></div>
<a class="link abs" href="#" style="left:259px;top:966px">VIEW AREAS</a>

<form class="quote-form abs">
  <div class="field">*First Name:</div>
  <div class="field">*Last Name:</div>
  <div class="field">*Email:</div>
  <div class="field">Phone:</div>
  <div class="field">City:</div>
  <div class="field">*Zip:</div>
  <div class="field">*County:</div>
  <div class="field">*Sq Ft:</div>
  <div class="field area">Comments:</div>
</form>
<div class="submit abs">SUBMIT</div>

<p class="testimonial abs">Many thanks for helping me with ordering the sod and please thank the team that installed the lawn. Your team were on time, quick, left the garden immaculate – and left a gorgeous looking lawn.</p>
<p class="author abs">MARLA T, RIVERTON:<br>OCT 2014</p>
<div class="rule abs"></div>
<a class="link abs" href="#" style="left:784px;top:964px">VIEW MORE</a>

<svg class="ground abs" viewBox="0 0 960 160" width="960" height="160">
  <polygon points="0,20 350,115 960,55 960,160 0,160" fill="#8cc158"/>
  <polygon points="0,60 350,115 960,40 960,160 0,160" fill="#a2d06c" opacity=".6"/>
  <polygon points="560,95 960,55 960,160 520,160" fill="#6fae38"/>
</svg>
<div class="banner abs">DON'T WORK FOR YOUR LAWN. JUST CHOOSE <b>VERDANT ROW</b> &amp; ENJOY YOUR LAWN &nbsp;→</div>
<div class="turf abs" role="img" aria-label="Rolled strip of fresh sod"></div>

<div class="foot-links abs">About Us &nbsp;/&nbsp; Services &nbsp;/&nbsp; Estimates &nbsp;/&nbsp; Contact Us<br>© 2014 VERDANTROW</div>
<div class="foot-brand abs">Verdant Row</div>
<div class="foot-brand-sub abs">WWW.VERDANTROW-EXAMPLE.COM<br>555-014-7720</div>
<div class="address abs">Verdant Row<br>P.O. Box 480<br>Lakeside, FL 30990</div>
<div class="foot-social abs"><i></i><i></i></div>

</body>
</html>
```